Building Company Business Card Design

Need a design for a business card:
It needs to have: Name, Phone, Social page link, Website, email
i would also like a list of works we undertake:
-New Homes
-Extensions, Renovations & Bathrooms
-Decking, Carports, Sheds (Residential and Industrial)
-Carpentry
-Fences, Patios & Pergolas

Name, Phone, Social page link, Website, email + details of services provided listed in description

```html
<!DOCTYPE html>
<html lang="en">
<head>
<meta charset="utf-8">
<title>Ridgeline Homes – Business Card</title>
<link href="https://fonts.googleapis.com/css2?family=Josefin+Sans:wght@600;700&display=swap" rel="stylesheet">
<style>
  :root {
    --green: #43b052;
    --black: #030405;
    --white: #ffffff;
    --bg-light: #ffffff;
    --bg-dark: #dcdcdc;
  }
  html, body {
    margin: 0;
    padding: 0;
    width: 1200px;
    height: 1200px;
    overflow: hidden;
  }
  body {
    background: radial-gradient(circle at 50% 50%, var(--bg-light) 0%, #f1f1f1 40%, var(--bg-dark) 100%);
    position: relative;
    font-family: "Josefin Sans", sans-serif;
  }
  .card {
    position: absolute;
    width: 829px;
    height: 536px;
    transform-origin: 0 0;
    transform: scale(0.621);
    background: var(--green);
    overflow: hidden;
    color: var(--white);
  }
  .card--front { left: 342px; top: 227px; }
  .card--back  { left: 345px; top: 672px; }
  .card__shape {
    position: absolute;
    inset: 0;
    width: 100%;
    height: 100%;
  }
  .services {
    position: absolute;
    left: 0; right: 0; top: 36px;
    text-align: center;
    font-weight: 600;
    font-size: 27px;
    line-height: 37px;
    letter-spacing: 0.6px;
    margin: 0;
    white-space: nowrap;
  }
  .brand-small {
    position: absolute;
    left: 0; right: 0; top: 278px;
    display: flex;
    justify-content: center;
    align-items: center;
    gap: 10px;
    font-weight: 700;
    font-size: 24px;
    letter-spacing: 2px;
    color: var(--green);
  }
  .brand-small__mark {
    width: 18px; height: 18px;
    background: var(--green);
  }
  .holder-name {
    position: absolute;
    left: 0; right: 0; top: 336px;
    text-align: center;
    font-weight: 700;
    font-size: 48px;
    line-height: 52px;
    margin: 0;
    white-space: nowrap;
  }
  .contact {
    position: absolute;
    display: flex;
    align-items: center;
    gap: 12px;
    font-weight: 700;
    font-size: 34px;
    letter-spacing: 0.5px;
    white-space: nowrap;
  }
  .contact svg { flex: none; }
  .contact--phone    { left: 78px;  top: 412px; }
  .contact--social   { left: 78px;  top: 460px; font-weight: 600; }
  .contact--web      { left: 418px; top: 412px; font-weight: 600; font-size: 31px; }
  .contact--email    { left: 418px; top: 460px; font-weight: 600; font-size: 31px; }
  .square-icon {
    width: 22px; height: 22px;
    background: var(--white);
    border-radius: 2px;
  }
  .brand-large {
    position: absolute;
    left: 104px; top: 122px;
    width: 625px;
    text-align: center;
    font-weight: 700;
    color: var(--white);
    white-space: nowrap;
  }
  .brand-large__mark {
    width: 90px; height: 90px;
    margin: 0 auto 62px;
    background: var(--green);
  }
  .brand-large__name {
    font-size: 60px;
    line-height: 58px;
    letter-spacing: 1px;
    margin: 0;
  }
  .brand-large__sub {
    font-size: 33px;
    line-height: 40px;
    letter-spacing: 0.5px;
    margin: 0;
  }
</style>
</head>
<body>

<section class="card card--front" aria-label="Business card front">
  <svg class="card__shape" viewBox="0 0 829 536" preserveAspectRatio="none" aria-hidden="true">
    <polygon points="0,209 267,209 829,314 829,536 0,536" fill="var(--black)"/>
  </svg>

  <p class="services">
    | New Homes | Extensions &nbsp;| Renovations &amp; Bathrooms |<br>
    | Decking &nbsp;| Carports |<br>
    | Sheds (Residential and Industrial) |<br>
    | Carpentry | Fences | Patios &amp; Pergolas |
  </p>

  <div class="brand-small">
    <span class="brand-small__mark"></span>
    <span>RIDGELINE</span>
  </div>

  <h1 class="holder-name">| Dale Whitford |</h1>

  <div class="contact contact--phone">
    <svg width="18" height="30" viewBox="0 0 18 30" aria-hidden="true">
      <rect x="1.5" y="1.5" width="15" height="27" rx="2.5" fill="none" stroke="#fff" stroke-width="2.5"/>
      <rect x="6" y="4" width="6" height="1.6" fill="#fff"/>
      <circle cx="9" cy="24.5" r="1.6" fill="#fff"/>
    </svg>
    <span>555.014.7720</span>
  </div>

  <div class="contact contact--social">
    <span class="square-icon"></span>
    <span>Social page link</span>
  </div>

  <div class="contact contact--web">
    <svg width="26" height="26" viewBox="0 0 26 26" aria-hidden="true" fill="none" stroke="#fff" stroke-width="1.8">
      <circle cx="13" cy="13" r="11"/>
      <ellipse cx="13" cy="13" rx="5" ry="11"/>
      <line x1="2" y1="13" x2="24" y2="13"/>
      <line x1="4" y1="7.5" x2="22" y2="7.5"/>
      <line x1="4" y1="18.5" x2="22" y2="18.5"/>
    </svg>
    <span>www.ridgeline.homes</span>
  </div>

  <div class="contact contact--email">
    <svg width="26" height="26" viewBox="0 0 26 26" aria-hidden="true" fill="none" stroke="#fff" stroke-width="1.8" stroke-linejoin="round">
      <path d="M4 22 L6 15 L18 3 L23 8 L11 20 Z"/>
      <line x1="15" y1="6" x2="20" y2="11"/>
      <line x1="2" y1="24" x2="10" y2="24"/>
    </svg>
    <span>ridgeline.homes@xxx.au</span>
  </div>
</section>

<section class="card card--back" aria-label="Business card back">
  <svg class="card__shape" viewBox="0 0 829 536" preserveAspectRatio="none" aria-hidden="true">
    <polygon points="0,0 565,0 563,474 0,421" fill="var(--black)"/>
  </svg>

  <div class="brand-large">
    <div class="brand-large__mark"></div>
    <p class="brand-large__name">RIDGELINE HOMES</p>
    <p class="brand-large__sub">AND DEVELOPMENTS PTY LTD</p>
  </div>
</section>

</body>
</html>
```